Business Card Design Project

Our organization is in need of a business card design with the use of our logo. We are looking for professional design that will embellish the image our consulting firm.

Here is a summary of what we do: Voltrane is systems consulting firm that specializes in the management, migration, and maintenance of IT infrastructure solutions.

Here is a link to my website: http://voltrane-example.com

I have attached the logo.

Target Market(s)

Organization that need IT and server support.

Industry/Entity Type

Business

```html
<!DOCTYPE html>
<html lang="en">
<head>
<meta charset="utf-8">
<title>Voltrane – Business Card</title>
<link rel="stylesheet" href="https://fonts.googleapis.com/css2?family=Questrial&display=swap">
<style>
  :root{
    --navy:#262f55;
    --orange:#e8772e;
    --ink:#3a3a3a;
    --paper:#ffffff;
    --bubble:#e6e7e8;
    --stage:#dfe4e6;
    --tag:#d96f2c;
  }
  *{margin:0;padding:0;box-sizing:border-box}
  html,body{width:1200px;height:960px;overflow:hidden}
  body{
    background:var(--stage);
    font-family:"Questrial", "Century Gothic", sans-serif;
    position:relative;
  }
  .card{
    position:absolute;
    left:280px;
    width:640px;height:366px;
    box-shadow:0 6px 18px rgba(0,0,0,.15);
    overflow:hidden;
  }
  /* Front */
  .card--front{top:88px;background:var(--paper)}
  .front__decor{
    position:absolute;left:0;top:0;width:250px;height:100%;
    background:radial-gradient(ellipse at 30% 75%, var(--bubble) 0%, rgba(230,231,232,.5) 45%, rgba(255,255,255,0) 75%);
  }
  .brand{
    position:absolute;left:250px;top:40px;
    display:flex;align-items:center;gap:26px;
  }
  .brand__dot{width:54px;height:54px;border-radius:50%;background:var(--navy)}
  .brand__rule{width:2px;height:108px;background:var(--orange)}
  .brand__name{font-size:54px;color:var(--navy);letter-spacing:-0.5px;line-height:1}
  .person{position:absolute;left:384px;top:176px;color:var(--ink)}
  .person__name{font-size:26px;letter-spacing:.5px;line-height:1.1}
  .person__title{font-size:15px;margin-top:4px}
  .contact{list-style:none;margin-top:18px;font-size:16px}
  .contact li{display:flex;align-items:center;gap:10px;height:22px}
  .contact svg{width:14px;height:14px;flex:none}
  .address{margin-top:14px;font-size:16px;line-height:1.35}
  /* Back */
  .card--back{top:506px;background:var(--navy);color:#fff}
  .back__brand{
    position:absolute;left:0;right:0;top:112px;
    display:flex;justify-content:center;align-items:center;gap:22px;
  }
  .back__dot{width:58px;height:58px;border-radius:50%;background:#fff}
  .back__name{font-size:60px;line-height:1}
  .back__tagline{
    position:absolute;left:0;right:0;top:262px;text-align:center;
    color:var(--tag);font-size:19px;letter-spacing:2.5px;
  }
</style>
</head>
<body>
  <section class="card card--front" aria-label="Business card front">
    <div class="front__decor" role="img" aria-label="Soft light grey bubble pattern"></div>
    <div class="brand">
      <span class="brand__dot"></span>
      <span class="brand__rule"></span>
      <span class="brand__name">voltrane</span>
    </div>
    <div class="person">
      <p class="person__name">MARCUS ELLERY</p>
      <p class="person__title">Managing Partner</p>
      <ul class="contact">
        <li>
          <svg viewBox="0 0 14 14" aria-hidden="true"><rect x="2" y="1" width="10" height="12" rx="1.5" fill="none" stroke="#e8772e" stroke-width="1.6"/><rect x="4.5" y="3.5" width="5" height="4" fill="#e8772e"/></svg>
          555.014.7301
        </li>
        <li>
          <svg viewBox="0 0 14 14" aria-hidden="true"><rect x="3.5" y="1" width="7" height="4" fill="#e8772e"/><rect x="1" y="5" width="12" height="6" rx="1" fill="#e8772e"/><rect x="3.5" y="9" width="7" height="4" fill="#fff" stroke="#e8772e" stroke-width="1.2"/></svg>
          555.014.7302
        </li>
        <li>
          <svg viewBox="0 0 14 14" aria-hidden="true"><circle cx="7" cy="7" r="6" fill="#e8772e"/><path d="M7 1v12M1 7h12M7 1c-3 3-3 9 0 12M7 1c3 3 3 9 0 12" fill="none" stroke="#fff" stroke-width="1"/></svg>
          voltrane-example.com
        </li>
      </ul>
      <p class="address">4180 Harbor Loop W<br>Riverton, TX 78099</p>
    </div>
  </section>

  <section class="card card--back" aria-label="Business card back">
    <div class="back__brand">
      <span class="back__dot"></span>
      <span class="back__name">voltrane</span>
    </div>
    <p class="back__tagline">SYSTEM SOLUTIONS</p>
  </section>
</body>
</html>
```